Elegant stationary design with logo

Looking for a simple elegant design incorporating the logo with similar colors. Will be used for PDFs and invoice templates. Rose gold, blush pink, copper hues are the colors. Final product to be able to be used as a template for word documents, PDFs, invoice, and training materials.

Target Market(s)

Small business owners mostly females.

Font styles to use
Serif
Script

Colors
feeeee
fee3d5

Requirements
Must have
• Colors and incorporate logo.
Nice to have
• Simple design with elegant edging.
Should not have
• Nothing too busy or techy.

```html
<!DOCTYPE html>
<html lang="en">
<head>
<meta charset="utf-8">
<title>Willow Bloom Studio — Stationery Set</title>
<link rel="stylesheet" href="https://fonts.googleapis.com/css2?family=Cinzel:wght@400&family=Arimo:wght@400;700&display=swap">
<style>
  :root {
    --backdrop: #616264;
    --paper: #ffffff;
    --copper: #c8886b;
    --blush-text: #d3a096;
    --ink: #c97f5f;
  }
  * { box-sizing: border-box; margin: 0; padding: 0; }
  html, body { width: 1059px; height: 1200px; overflow: hidden; }
  body { background: var(--backdrop); position: relative; font-family: "Arimo", Arial, sans-serif; }

  .sheet { position: absolute; background: var(--paper); overflow: hidden; }
  .sheet .edge { position: absolute; inset: 0; width: 100%; height: 100%; }
  .edge path { fill: var(--copper); }

  .letterhead { left: 229px; top: 48px; width: 601px; height: 776px; }
  .envelope { left: 225px; top: 846px; width: 611px; height: 306px; }
  .card { box-shadow: 2px 3px 4px rgba(0,0,0,.35); }
  .card-front { left: 574px; top: 237px; width: 248px; height: 136px; }
  .card-back { left: 578px; top: 425px; width: 247px; height: 141px; }

  .brand { position: absolute; display: flex; flex-direction: column; align-items: center; transform: translateX(-50%); }
  .brand-dot { border: 2px solid var(--copper); border-radius: 50%; }
  .brand-name { font-family: "Cinzel", Georgia, serif; font-weight: 400; color: var(--blush-text); text-align: center; line-height: 1; white-space: nowrap; }
  .brand-name span { display: block; }
  .brand-name .brand-sub { font-size: .55em; margin-top: .15em; letter-spacing: .04em; }

  .contact { position: absolute; list-style: none; color: var(--ink); }
  .contact li { display: flex; align-items: center; white-space: nowrap; }
  .contact svg { fill: var(--ink); flex: none; }
  .contact .phone-number { letter-spacing: .22em; }

  .contact-large { font-size: 10.5px; }
  .contact-large li { height: 15.8px; }
  .contact-large svg { width: 8px; height: 8px; margin-right: 6px; }

  .contact-small { font-size: 6.3px; }
  .contact-small li { height: 12.6px; }
  .contact-small svg { width: 6px; height: 6px; margin-right: 6px; }
  .contact-small .phone-number { letter-spacing: 0; }

  .holder { position: absolute; left: 144px; top: 23px; color: var(--ink); }
  .holder-name { font-weight: 700; font-size: 7.4px; letter-spacing: .03em; }
  .holder-role { font-size: 5px; margin-top: 2px; letter-spacing: .04em; }
</style>
</head>
<body>
<svg width="0" height="0" style="position:absolute">
  <symbol id="icon-phone" viewBox="0 0 10 10"><path d="M2 0.5 L3.6 0.5 L4.2 2.8 L3 3.6 C3.6 5 4.8 6.3 6.3 7 L7.1 5.8 L9.5 6.4 L9.5 8 C9.5 9 8.7 9.6 7.8 9.5 C4 9 0.9 5.9 0.5 2.2 C0.4 1.2 1 0.5 2 0.5 Z"/></symbol>
  <symbol id="icon-mail" viewBox="0 0 10 10"><path d="M0.5 3.5 L5 1 L9.5 3.5 L9.5 9 L0.5 9 Z M1.5 4 L5 6.3 L8.5 4 L8.5 3.8 L5 2 L1.5 3.8 Z" fill-rule="evenodd"/></symbol>
  <symbol id="icon-globe" viewBox="0 0 10 10"><path d="M5 0.5 A4.5 4.5 0 1 0 5.01 0.5 Z M5 1.5 A3.5 3.5 0 1 1 4.99 1.5 Z M4.5 1 L5.5 1 L5.5 9 L4.5 9 Z M1 4.5 L9 4.5 L9 5.5 L1 5.5 Z M5 1 C2.8 3 2.8 7 5 9 L5 8.2 C3.6 6.5 3.6 3.5 5 1.8 Z M5 1 C7.2 3 7.2 7 5 9 L5 8.2 C6.4 6.5 6.4 3.5 5 1.8 Z" fill-rule="evenodd"/></symbol>
  <symbol id="icon-pin" viewBox="0 0 10 10"><path d="M5 0.3 C2.9 0.3 1.5 1.8 1.5 3.7 C1.5 6.2 5 9.8 5 9.8 C5 9.8 8.5 6.2 8.5 3.7 C8.5 1.8 7.1 0.3 5 0.3 Z M5 2.3 A1.4 1.4 0 1 0 5.01 2.3 Z" fill-rule="evenodd"/></symbol>
</svg>

<section class="sheet letterhead" aria-label="Letterhead">
  <svg class="edge" viewBox="0 0 751 970" preserveAspectRatio="none">
    <path d="M0 2 C320 -4 660 25 751 130 L751 0 L0 0 Z"/>
    <path d="M0 838 C110 930 320 965 520 970 L0 970 Z"/>
  </svg>
  <div class="brand" style="left:107px; top:22px;">
    <div class="brand-dot" style="width:62px; height:62px;"></div>
    <div class="brand-name" style="font-size:18px; margin-top:6px;"><span>Willow Bloom</span><span class="brand-sub">Studio</span></div>
  </div>
  <ul class="contact contact-large" style="left:461px; top:696px;">
    <li><svg><use href="#icon-phone"/></svg><span class="phone-number">123.456.7890</span></li>
    <li><svg><use href="#icon-mail"/></svg>lorem@ipsum.com</li>
    <li><svg><use href="#icon-globe"/></svg>www.loremipsum.com</li>
    <li><svg><use href="#icon-pin"/></svg>000 loremipsum street</li>
  </ul>
</section>

<section class="sheet card card-front" aria-label="Business card front">
  <svg class="edge" viewBox="0 0 310 170" preserveAspectRatio="none">
    <path d="M0 0 C150 -2 265 15 310 62 L310 0 Z"/>
    <path d="M0 110 C40 150 130 168 240 170 L0 170 Z"/>
  </svg>
  <div class="brand" style="left:48px; top:20px;">
    <div class="brand-dot" style="width:26px; height:26px; border-width:1px;"></div>
    <div class="brand-name" style="font-size:8px; margin-top:3px;"><span>Willow Bloom</span><span class="brand-sub">Studio</span></div>
  </div>
  <div class="holder">
    <div class="holder-name">LOREM IPSUM</div>
    <div class="holder-role">DIRECTOR</div>
  </div>
  <ul class="contact contact-small" style="left:146px; top:73px;">
    <li><svg><use href="#icon-phone"/></svg><span class="phone-number">123.456.7890</span></li>
    <li><svg><use href="#icon-mail"/></svg>loremipsum@loremi.com</li>
    <li><svg><use href="#icon-globe"/></svg>www.loremipsum.com</li>
    <li><svg><use href="#icon-pin"/></svg>000 loremipsum street</li>
  </ul>
</section>

<section class="sheet card card-back" aria-label="Business card back">
  <svg class="edge" viewBox="0 0 310 177" preserveAspectRatio="none">
    <path d="M0 0 C150 -2 265 15 310 62 L310 0 Z"/>
    <path d="M0 115 C40 155 130 175 240 177 L0 177 Z"/>
  </svg>
  <div class="brand" style="left:124px; top:40px;">
    <div class="brand-dot" style="width:38px; height:38px; border-width:1.5px;"></div>
    <div class="brand-name" style="font-size:11px; margin-top:4px;"><span>Willow Bloom</span><span class="brand-sub">Studio</span></div>
  </div>
</section>

<section class="sheet envelope" aria-label="Envelope">
  <svg class="edge" viewBox="0 0 764 383" preserveAspectRatio="none">
    <path d="M0 2 C330 -4 680 20 764 133 L764 0 L0 0 Z"/>
    <path d="M0 248 C90 340 300 380 480 383 L0 383 Z"/>
  </svg>
  <div class="brand" style="left:89px; top:33px;">
    <div class="brand-dot" style="width:48px; height:48px;"></div>
    <div class="brand-name" style="font-size:15px; margin-top:5px;"><span>Willow Bloom</span><span class="brand-sub">Studio</span></div>
  </div>
  <ul class="contact contact-large" style="left:468px; top:222px;">
    <li><svg><use href="#icon-phone"/></svg><span class="phone-number">123.456.7890</span></li>
    <li><svg><use href="#icon-mail"/></svg>lorem@ipsum.com</li>
    <li><svg><use href="#icon-globe"/></svg>www.loremipsum.com</li>
    <li><svg><use href="#icon-pin"/></svg>000 loremipsum street</li>
  </ul>
</section>
</body>
</html>
```